Vorel constructions

We are predominantly a residential home builder based in Melbourne, Victoria Australia. We construct houses, apartments, townhouses, multi-unit developments.

The name of the company is "Vorel Constructions"
My company believes in building unique construction projects mainly residential homes. The target customers are upmarket Melbourne residents/investors.

I want the brand name "Vorel" to be part of the logo. There's no need to put the word construction in the logo at this stage.

I would also like some ideas for a slogan e.g. "Just build it." or "We build quality homes." But I would like something unique and different for a slogan not the same old cliche.

vorelconstructions.example.com.au
e: tmelo@vorelconstructions.example.com.au
M: 0417305862
Address: 8/3 Fenwick Lane Marrowby VIC 3999

Director:Mr Dinesh Malarkodiyan

```html
<!DOCTYPE html>
<html lang="en">
<head>
<meta charset="utf-8">
<title>Vorel Constructions – Business Card</title>
<link rel="stylesheet" href="https://fonts.googleapis.com/css2?family=Arimo:wght@400;700&display=swap">
<style>
  :root {
    --backdrop: #d6d9dc;
    --card: #2a2828;
    --card-edge: #333131;
    --accent: #1db2e3;
    --ink: #f2f2f2;
    --muted: #d8d8d8;
  }
  * { box-sizing: border-box; margin: 0; padding: 0; }
  html, body {
    width: 1200px; height: 1041px; overflow: hidden;
    background: var(--backdrop);
    font-family: "Arimo", Arial, sans-serif;
  }
  .card {
    position: absolute; left: 180px; width: 840px; height: 466px;
    background: radial-gradient(ellipse at 55% 40%, var(--card-edge), var(--card) 70%);
    box-shadow: 0 6px 18px rgba(0,0,0,.25);
    overflow: hidden;
  }
  .card--front { top: 40px; }
  .card--back { top: 535px; }

  .rule { position: absolute; background: var(--accent); }
  .card--front .rule--left { left: 0; top: 214px; width: 262px; height: 3px; }
  .card--front .rule--right { left: 606px; top: 176px; width: 234px; height: 3px; }

  .wordmark {
    position: absolute; display: flex; align-items: center; gap: 12px;
    color: var(--accent); font-weight: 700; line-height: 1;
  }
  .wordmark__square { background: var(--ink); }
  .card--front .wordmark { left: 292px; top: 140px; font-size: 92px; }
  .card--front .wordmark__square { width: 22px; height: 22px; }

  .tagline {
    position: absolute; left: 430px; top: 246px;
    color: var(--ink); font-size: 24px; letter-spacing: 1.5px;
  }

  .card--back .rule--top { left: 112px; top: 0; width: 3px; height: 168px; }
  .card--back .rule--bottom { left: 52px; top: 402px; width: 3px; height: 64px; }
  .card--back .wordmark { right: 70px; top: 82px; font-size: 104px; }
  .card--back .wordmark__square { width: 24px; height: 24px; }

  .person { position: absolute; left: 96px; top: 178px; font-size: 23px; color: var(--ink); line-height: 1.15; }
  .person__name { color: var(--accent); }

  .contact { position: absolute; left: 86px; top: 262px; list-style: none; }
  .contact li {
    display: flex; align-items: center; gap: 14px;
    color: var(--muted); font-size: 17px; letter-spacing: 2px; line-height: 24px;
    white-space: nowrap;
  }
  .contact svg { width: 14px; height: 14px; fill: none; stroke: var(--muted); stroke-width: 1.6; flex: none; }
  .contact .accent { color: var(--accent); }
</style>
</head>
<body>

<section class="card card--front" aria-label="Card front">
  <span class="rule rule--left"></span>
  <span class="rule rule--right"></span>
  <div class="wordmark"><span class="wordmark__square"></span>Vorel</div>
  <p class="tagline">We Build Quality Homes.</p>
</section>

<section class="card card--back" aria-label="Card back">
  <span class="rule rule--top"></span>
  <span class="rule rule--bottom"></span>
  <div class="wordmark"><span class="wordmark__square"></span>Vorel</div>

  <p class="person">Mr <span class="person__name">Dinesh Malarkodiyan</span><br>Director</p>

  <ul class="contact">
    <li><svg viewBox="0 0 14 14"><rect x="3.5" y="1" width="7" height="12" rx="1"/><line x1="6" y1="11" x2="8" y2="11"/></svg><span>0417305862</span></li>
    <li><svg viewBox="0 0 14 14"><rect x="1" y="3" width="12" height="8"/><polyline points="1,3 7,8 13,3"/></svg><span>tmelo@vorelconstructions.example.com.au</span></li>
    <li><svg viewBox="0 0 14 14"><circle cx="7" cy="7" r="5.5"/><ellipse cx="7" cy="7" rx="2.3" ry="5.5"/><line x1="1.5" y1="7" x2="12.5" y2="7"/></svg><span>www.<span class="accent">VorelConstructions</span>.example.com.au</span></li>
    <li><svg viewBox="0 0 14 14"><path d="M7 13 C3 8 3 6.5 3 5.5 a4 4 0 0 1 8 0 C11 6.5 11 8 7 13Z"/><circle cx="7" cy="5.5" r="1.3"/></svg><span>8/3 Fenwick Lane Marrowby VIC 3999</span></li>
  </ul>
</section>

</body>
</html>
```